Varolta Business Card

I am looking for a business card design for a start-up company called Varolta Group. This is a management consultancy focused on sales, marketing, sales management, product management and AGILE software development. Our primary customers are $1M to $50M in revenue.

Varolta is the Italian word for "slope."

The path from $0 to $50M has many different growth stages associated with it. Each one having a significant slope to the next plateau. Our expertise helps our customers ascend each of those slopes. We bring experience, successful track-records in growing companies, best practices and a dive-in and roll-up your sleeves mentality. We are not sitting at base camp shouting instructions, we are right there with you, on the climb.

Industry/Entity Type

Business

```html
<!DOCTYPE html>
<html lang="en">
<head>
<meta charset="utf-8">
<title>Varolta Business Card</title>
<link href="https://fonts.googleapis.com/css2?family=Questrial&display=swap" rel="stylesheet">
<style>
  :root {
    --stage: #000000;
    --blue-light: #00a6e4;
    --blue-mid: #0a6fb5;
    --blue-deep: #003f7d;
    --green-light: #7fb838;
    --green-deep: #4a7d27;
    --mark: #6aa832;
    --white: #ffffff;
    --muted: #d9ecc4;
  }
  * { margin: 0; padding: 0; box-sizing: border-box; }
  html, body {
    width: 1200px; height: 1000px; overflow: hidden;
    background: var(--stage);
    font-family: "Questrial", "Helvetica Neue", Arial, sans-serif;
    color: var(--white);
  }
  .canvas { position: relative; width: 1200px; height: 1000px; }
  .card {
    position: absolute; top: 187px;
    width: 345px; height: 586px; overflow: hidden;
  }
  .card--front {
    left: 237px;
    background: linear-gradient(160deg, var(--blue-mid) 0%, #0b8fd0 45%, var(--blue-deep) 100%);
  }
  .card--back {
    left: 660px;
    background: radial-gradient(circle at 85px 83px, var(--blue-light) 0%, var(--blue-mid) 50%, var(--blue-deep) 100%);
  }
  .card__band {
    position: absolute; left: 0; right: 0; bottom: 0;
    background: linear-gradient(180deg, var(--green-light) 0%, var(--green-deep) 100%);
  }
  .card--front .card__band { top: 330px; }
  .card--back .card__band { height: 22px; }

  .brand { position: absolute; display: flex; align-items: center; }
  .brand__dot { border-radius: 50%; background: var(--mark); flex: none; }
  .brand__name { font-weight: 400; color: var(--white); letter-spacing: -0.5px; line-height: 1; }

  .card--front .brand { left: 43px; top: 36px; gap: 12px; }
  .card--front .brand__dot { width: 58px; height: 58px; }
  .card--front .brand__name { font-size: 52px; }

  .card--back .brand {
    left: 0; right: 0; top: 140px;
    flex-direction: column; gap: 22px;
  }
  .card--back .brand__dot { width: 96px; height: 96px; }
  .card--back .brand__name { font-size: 48px; }

  .holder { position: absolute; left: 41px; top: 368px; }
  .holder__name { font-size: 24px; line-height: 1.1; }
  .holder__role { font-size: 17px; color: var(--muted); line-height: 1.2; }

  .contact {
    position: absolute; left: 41px; top: 451px;
    list-style: none; font-size: 15.5px; line-height: 20.2px;
  }
  .contact li::before {
    content: ""; display: inline-block;
    width: 6px; height: 6px; border-radius: 50%;
    background: var(--white); margin-right: 6px; vertical-align: middle;
    position: relative; top: -1px;
  }
</style>
</head>
<body>
<main class="canvas">

  <section class="card card--front" aria-label="Business card front">
    <div class="card__band"></div>

    <div class="brand">
      <span class="brand__dot"></span>
      <span class="brand__name">Varolta</span>
    </div>

    <div class="holder">
      <p class="holder__name">Marco Bellini</p>
      <p class="holder__role">President</p>
    </div>

    <ul class="contact">
      <li>www.varolta.com</li>
      <li>bellini@varolta.com</li>
      <li>phone: +310.555.0142</li>
      <li>mob: 714.555.0187</li>
      <li>52 Ridgeview Plaza, Suite 204 Lakeport</li>
    </ul>
  </section>

  <section class="card card--back" aria-label="Business card back">
    <div class="card__band"></div>

    <div class="brand">
      <span class="brand__dot"></span>
      <span class="brand__name">Varolta</span>
    </div>
  </section>

</main>
</body>
</html>
```